Velmora EIRL Business Card Design Project

We need a business card design for a New Business Intelligence Consultant. We bring a complete service to the client from first consulting meeting to help desk and system improvement.

I will upload the company logo and I like to use the logo colors on the card. Feel free to use all logo components on the design, for example one side with the black logo using complete card and the other side only the red shape (is an example, feel absolutely free :)).

The principal idea is to sell a professional service and a modern company.

Target Market(s)

IT Business Intelligence Clients

Industry/Entity Type

Professional Service

Requirements
Nice to have
• - Use the logo colors and minimize white sections.
- Rounded borders
Should not have
• I don't want to see any references to people working on a meeting or office photos or any computers related logos.

```html
<!DOCTYPE html>
<html lang="en">
<head>
<meta charset="utf-8">
<title>Velmora EIRL – Business Card</title>
<link rel="stylesheet" href="https://fonts.googleapis.com/css2?family=Source+Sans+3:wght@400;600;700&display=swap">
<style>
  :root {
    --bg: #e9e6e1;
    --card: #ffffff;
    --red: #ed1c24;
    --grey: #6d6e71;
    --ink: #1a1a1a;
  }
  html, body {
    margin: 0;
    padding: 0;
    width: 945px;
    height: 1200px;
    overflow: hidden;
    background: var(--bg);
    font-family: "Source Sans 3", "Myriad Pro", Arial, sans-serif;
    color: var(--ink);
  }
  .canvas {
    position: relative;
    width: 945px;
    height: 1200px;
  }
  .card {
    position: absolute;
    left: 20px;
    width: 868px;
    height: 497px;
    background: var(--card);
    border-radius: 30px;
    overflow: hidden;
  }
  .card--front { top: 63px; }
  .card--back  { top: 669px; }

  .brand {
    position: absolute;
    left: 0;
    right: 0;
    display: flex;
    align-items: center;
    justify-content: center;
    gap: 26px;
    color: var(--red);
    font-weight: 600;
    line-height: 1;
  }
  .brand__mark {
    background: var(--grey);
  }
  .card--front .brand { top: 70px; font-size: 112px; }
  .card--front .brand__mark { width: 92px; height: 92px; }
  .card--back .brand { top: 158px; font-size: 60px; gap: 16px; }
  .card--back .brand__mark { width: 50px; height: 50px; }

  .person {
    position: absolute;
    top: 235px;
    left: 0;
    right: 0;
    text-align: center;
    font-size: 28px;
  }
  .person__name { font-weight: 700; font-size: 37px; }
  .person__sep { margin: 0 4px; }

  .contact {
    position: absolute;
    top: 330px;
    left: 0;
    right: 0;
    text-align: center;
    font-size: 23px;
    line-height: 32px;
  }
  .contact p { margin: 0; }
  .contact b { font-weight: 700; }

  .web {
    position: absolute;
    top: 290px;
    left: 0;
    right: 0;
    text-align: center;
    font-size: 27px;
  }

  .bands {
    position: absolute;
    left: 0;
    bottom: 0;
    width: 868px;
    height: 49px;
    display: block;
  }
  .bands__red  { fill: var(--red); }
  .bands__grey { fill: var(--grey); }
</style>
</head>
<body>
<main class="canvas">

  <section class="card card--front">
    <div class="brand">
      <span class="brand__mark"></span>
      <span class="brand__name">Velmora</span>
    </div>
    <div class="person">
      <span class="person__name">First Name</span><span class="person__sep">|</span><span class="person__role">Founder</span>
    </div>
    <div class="contact">
      <p><b>Phone.</b> 001-5550147 <b>Fax.</b> 001-5550182 <b>Cell.</b> 5550193846</p>
      <p><b>Email.</b> hello@velmora-bi.com <b>Web.</b> www.velmora-bi.com</p>
      <p>01, Street Name, State, Country</p>
    </div>
    <svg class="bands" viewBox="0 0 868 49" aria-hidden="true">
      <polygon class="bands__red" points="0,0 456,0 439,49 0,49"/>
      <polygon class="bands__grey" points="465,0 868,0 868,49 448,49"/>
    </svg>
  </section>

  <section class="card card--back">
    <div class="brand">
      <span class="brand__mark"></span>
      <span class="brand__name">Velmora</span>
    </div>
    <div class="web">www.velmora-bi.com</div>
    <svg class="bands" viewBox="0 0 868 49" aria-hidden="true">
      <polygon class="bands__red" points="0,0 456,0 439,49 0,49"/>
      <polygon class="bands__grey" points="465,0 868,0 868,49 448,49"/>
    </svg>
  </section>

</main>
</body>
</html>
```